Fox & Fig honey company needs a label design.

We need a label design for a new honey company, based in the state of Florida called 'Fox & Fig". We are supplying our online customers with the highest quality of the various kinds of raw honey. Our product is honey in the oval hexagon glass jar with black lid. We would like to see designs that use black background with gold font .
In the upper part of the label is gold flying Honey Bee (profile, silhouette). The name of the brand "Fox & Fig" - Caramel font. Additional fonts are Cinzel, Source Sans Pro. Label measurements 2.6" by 3".
Label content:
Fox & Fig
RAW HONEY
wildflower
PURE & NATURAL
made by Florida Bees
foxandfigjars.com
NET WT 12oz (340g)

The final design should have eye catching, luxurious look.
Updates

Need extra days to review

Target Market(s)

Luxury

Industry/Entity Type

Food (bee products)

Font styles to use
Other font styles liked:
• caramel

Colors

Designer to choose colors to be used in the design.

Requirements
Must have
• Gold letters on black background, Drawing of a bee, flying in profile

```html
<!DOCTYPE html>
<html lang="en">
<head>
<meta charset="utf-8">
<title>Fox &amp; Fig Raw Honey Label</title>
<link rel="stylesheet" href="https://fonts.googleapis.com/css2?family=Cinzel:wght@400;600&family=Source+Sans+3:wght@400;600&display=swap">
<style>
  :root {
    --backdrop: #dcdcdc;
    --label-black: #030303;
    --gold: #c8872e;
    --gold-light: #e6b45c;
    --gold-deep: #8f5418;
    --bronze-frame: #b06f28;
    --ink-dark: #1a0f05;
  }
  * { box-sizing: border-box; margin: 0; padding: 0; }
  html, body {
    width: 1200px; height: 1200px; overflow: hidden;
    background: var(--backdrop);
  }
  .canvas {
    position: relative; width: 1200px; height: 1200px;
    background: radial-gradient(circle at 50% 45%, #ececec 0%, var(--backdrop) 75%);
  }
  .label-wrap {
    position: absolute; left: 80px; top: 217px;
    width: 1040px; height: 767px;
    background: var(--label-black);
  }
  .front-panel {
    position: absolute; left: 278px; top: 66px;
    width: 504px; height: 620px;
    border: 4px solid var(--bronze-frame);
  }
  .bee-illustration {
    position: absolute; left: 275px; top: -110px;
    width: 195px; height: 150px;
    border-radius: 50%;
    background: radial-gradient(ellipse at 50% 50%, #9a5a26 0%, #d9a24a 45%, rgba(230,180,92,0) 72%);
  }
  .brand-name {
    position: absolute; left: 0; right: 0; top: 95px;
    text-align: center;
    font-family: "Cinzel", serif; font-weight: 600;
    font-size: 66px; color: var(--gold);
    letter-spacing: 1px;
  }
  .honey-seal {
    position: absolute; left: 102px; top: 240px;
    width: 300px; height: 170px;
  }
  .honey-seal .arc-text {
    font-family: "Cinzel", serif; font-size: 24px;
    fill: var(--gold); letter-spacing: 1px;
  }
  .honey-seal .seal-word {
    font-family: "Cinzel", serif; font-size: 42px;
    fill: var(--ink-dark); text-anchor: middle;
  }
  .origin-line {
    position: absolute; left: 0; right: 0; top: 433px;
    text-align: center;
    font-family: "Source Sans 3", sans-serif; font-size: 31px;
    color: var(--gold); letter-spacing: -0.8px;
  }
  .net-weight {
    position: absolute; left: 0; right: 0; top: 485px;
    text-align: center;
    font-family: "Source Sans 3", sans-serif; font-size: 18px;
    color: var(--gold);
  }
  .small-bees {
    position: absolute; left: 78px; top: 505px;
    width: 85px; height: 85px; border-radius: 50%;
    background: radial-gradient(ellipse at 50% 50%, #b9782c 0%, rgba(200,135,46,0) 70%);
  }
  .web-band {
    position: absolute; left: 0; right: 0; bottom: 0; height: 54px;
    background: linear-gradient(90deg, var(--gold-deep) 0%, var(--gold-light) 25%, var(--gold) 55%, var(--gold-light) 80%, var(--gold-deep) 100%);
    display: flex; align-items: center; justify-content: center;
    padding-left: 50px;
    font-family: "Source Sans 3", sans-serif; font-weight: 600;
    font-size: 26px; color: var(--ink-dark);
  }
</style>
</head>
<body>
<div class="canvas">
  <div class="label-wrap">
    <div class="front-panel">
      <div class="bee-illustration" role="img" aria-label="Gold honey bee illustration in flight"></div>
      <div class="brand-name">Fox &amp; Fig</div>
      <svg class="honey-seal" viewBox="0 0 300 170" aria-label="Pure and natural raw honey">
        <defs>
          <radialGradient id="sealGold" cx="45%" cy="35%" r="70%">
            <stop offset="0%" stop-color="#f0c46a"/>
            <stop offset="55%" stop-color="#c8872e"/>
            <stop offset="100%" stop-color="#7a4412"/>
          </radialGradient>
          <path id="sealArc" d="M 25 118 A 128 100 0 0 1 275 118"/>
        </defs>
        <text class="arc-text"><textPath href="#sealArc" startOffset="50%" text-anchor="middle">PURE &amp; NATURAL</textPath></text>
        <ellipse cx="150" cy="112" rx="110" ry="53" fill="url(#sealGold)"/>
        <text class="seal-word" x="150" y="107">RAW</text>
        <text class="seal-word" x="150" y="144">HONEY</text>
      </svg>
      <div class="origin-line">Made by Florida Bees</div>
      <div class="net-weight">NET WT 12oz (340g)</div>
      <div class="web-band">foxandfigjars.com</div>
      <div class="small-bees" role="img" aria-label="Two small gold bee illustrations"></div>
    </div>
  </div>
</div>
</body>
</html>
```